Visitenkarten-Design für italienisches Küchenschiff
Zielgruppe
Restaurantschiff Ilvora
Aufgabenstellung
Wir sind ein italienische Küche Schiff auf der Binnenalster in Hamburg und wollen den schönen Blick und gerne auch die italienischen Farben widerspiegeln...ich brauche das einmal neutral für den normalen Gast....und würde das denn..wenn es denn gut wird...auch gerne individell mit m e i n e r Tel Nr und auch für meine führenden Mitarbeiter personalisieren...aber...zuerst natürlich das neutrale...dazu schicke ich die alte Karte mit dem auch alten Logo was nicht unbedingt verwendet werden muss...

```html
<!DOCTYPE html>
<html lang="de">
<head>
<meta charset="utf-8">
<title>Visitenkarte Schiffsrestaurant Ilvora</title>
<link href="https://fonts.googleapis.com/css2?family=Advent+Pro:wght@300;400&display=swap" rel="stylesheet">
<style>
  :root {
    --stage: #4b4b4b;
    --paper: #ffffff;
    --ink: #7d7468;
    --green: #0f9a5a;
    --grey: #c8c8c8;
    --red: #a4262c;
    --map: #ddd3c1;
    --night: #5a4d5c;
    --cabin: #6f8a9a;
  }
  * { margin: 0; padding: 0; box-sizing: border-box; }
  html, body { width: 1200px; height: 1200px; overflow: hidden; }
  body {
    background: var(--stage);
    position: relative;
    font-family: "Advent Pro", "Arial Narrow", sans-serif;
    font-weight: 300;
    color: var(--ink);
  }
  .card {
    position: absolute;
    width: 510px;
    height: 329px;
    background: var(--paper);
    box-shadow: 5px 5px 7px rgba(0,0,0,0.45);
    overflow: hidden;
  }
  .card--front { left: 61px; top: 457px; }
  .card--back { left: 629px; top: 458px; }

  .flag-side { position: absolute; left: 0; top: 0; width: 14px; height: 100%; display: flex; flex-direction: column; }
  .flag-side span { flex: 1; }
  .green { background: var(--green); }
  .grey { background: var(--grey); }
  .red { background: var(--red); }

  .location-map {
    position: absolute; left: 14px; top: 0; width: 221px; height: 100%;
    background: linear-gradient(160deg, #e6dece 0%, var(--map) 55%, #c9bead 100%);
  }

  .brand {
    position: absolute; left: 262px; top: 82px;
    font-size: 40px; line-height: 1; letter-spacing: 1px;
    font-weight: 300;
  }
  .brand-sub {
    position: absolute; left: 262px; top: 129px;
    font-size: 18px; letter-spacing: 1.6px; line-height: 1;
  }
  .contact { position: absolute; left: 262px; top: 160px; font-size: 16.5px; line-height: 19.6px; }
  .contact .head { font-size: 18px; margin-top: 5px; }
  .contact .label { display: inline-block; width: 34px; }

  .photo { position: absolute; left: 22px; width: 211px; }
  .photo--cabin { top: 19px; height: 128px; background: linear-gradient(180deg, #8a6b4a 0%, var(--cabin) 25%, #7c9aab 55%, #b9333a 75%, #eeeeee 100%); }
  .photo--night { top: 162px; height: 125px; background: linear-gradient(180deg, #8a7283 0%, var(--night) 50%, #3a3a45 75%, #2b2b35 100%); }

  .info { position: absolute; left: 257px; font-size: 16.5px; line-height: 21px; }
  .info h2 { font-weight: 300; font-size: 21px; line-height: 1; margin-bottom: 8px; }
  .info--hours { top: 52px; width: 220px; }
  .hours-row { display: flex; justify-content: space-between; }
  .hours-row.kitchen { justify-content: flex-end; margin-top: 4px; }
  .info--booking { top: 174px; width: 245px; }

  .flag-bottom { position: absolute; left: 0; top: 300px; width: 100%; height: 9px; display: flex; }
  .flag-bottom span { flex: 1; }
</style>
</head>
<body>
  <section class="card card--front">
    <div class="flag-side"><span class="green"></span><span class="grey"></span><span class="red"></span></div>
    <div class="location-map" role="img" aria-label="Stadtplan-Ausschnitt an der Binnenalster mit Standortmarkierung des Restaurantschiffs"></div>
    <div class="brand">ILVORA</div>
    <div class="brand-sub">Schiffsrestaurant Ilvora</div>
    <div class="contact">
      <div>Seelindamm (Wasserseite)</div>
      <div>21874 Hamburg</div>
      <div class="head">Kontakt</div>
      <div><span class="label">Tel:</span>+49 040 / 55 18 43</div>
      <div><span class="label">Fax:</span>+49 040 / 55 18 4</div>
      <div>www.alsterschiff-ilvora.com</div>
      <div>E-Mail: info(at)alsterschiff-ilvora.com</div>
    </div>
  </section>

  <section class="card card--back">
    <div class="photo photo--cabin" role="img" aria-label="Foto: gedeckter Tisch im Salon des Schiffs mit Blick durch die Fenster auf die Alster"></div>
    <div class="photo photo--night" role="img" aria-label="Foto: beleuchtete Uferpromenade der Binnenalster bei Nacht mit Spiegelungen im Wasser"></div>
    <div class="info info--hours">
      <h2>Öffnungszeiten</h2>
      <div class="hours-row"><span>Montag - Sonntag</span><span>12:00 - 23:00</span></div>
      <div class="hours-row kitchen"><span>Küche bis 22:00</span></div>
    </div>
    <div class="info info--booking">
      <h2>Reservierungen</h2>
      <p>Wollen Sie einen Tisch reservieren? Wir freuen uns auf Ihren Anruf oder eine: reservierung(at)alsterschiff-ilvora.com</p>
    </div>
    <div class="flag-bottom"><span class="green"></span><span class="grey"></span><span class="red"></span></div>
  </section>
</body>
</html>
```